Banner and logo redesign for B2B website

I want a new email banner design and logo. This is for a B2B whitepaper library hosting content and resources of technology companies.https://ml.vexomarlin.net/

Target Market(s)

B2B

Industry/Entity Type

tech B2B

Number of Pages Required

1 page

Font styles to use
Sans Serif

Requirements
Must have
• A logo and email banner
Nice to have
• Similar colour pallet to what can be found on the site
Should not have
• website designs

```html
<!DOCTYPE html>
<html lang="en">
<head>
<meta charset="utf-8">
<title>Vexomarlin Email Banner</title>
<link rel="stylesheet" href="https://fonts.googleapis.com/css2?family=Montserrat:wght@400;500;600&display=swap">
<style>
  :root {
    --page-bg: #f6f5fd;
    --banner-bg: #eeebfd;
    --navy: #0f1a45;
    --violet: #5a4ff0;
    --text: #1e2550;
    --ribbon-a: #c9d3fb;
    --ribbon-b: #7b6ef2;
    --ribbon-c: #c056d8;
  }
  * { margin: 0; padding: 0; box-sizing: border-box; }
  html, body {
    width: 1200px;
    height: 581px;
    overflow: hidden;
    background: var(--page-bg);
    font-family: "Montserrat", sans-serif;
  }
  .email-banner {
    position: absolute;
    left: 64px;
    top: 149px;
    width: 1078px;
    height: 350px;
    background: var(--banner-bg);
    overflow: hidden;
  }
  .ribbon-art {
    position: absolute;
    left: 36px;
    top: 0;
    width: 318px;
    height: 350px;
    background: linear-gradient(160deg, var(--ribbon-a) 0%, var(--ribbon-b) 45%, var(--ribbon-c) 70%, var(--ribbon-a) 100%);
    opacity: 0.55;
    border-radius: 0 140px 0 160px;
  }
  .brand {
    position: absolute;
    left: 399px;
    top: 70px;
    display: flex;
    align-items: center;
    gap: 22px;
  }
  .brand-dot {
    width: 78px;
    height: 78px;
    border-radius: 50%;
    background: var(--violet);
  }
  .brand-name {
    font-size: 60px;
    font-weight: 600;
    letter-spacing: 2px;
    color: var(--navy);
  }
  .contact-list {
    position: absolute;
    left: 405px;
    top: 214px;
    display: grid;
    grid-template-columns: 334px 300px;
    row-gap: 14px;
    list-style: none;
  }
  .contact-item {
    display: flex;
    align-items: flex-start;
    gap: 14px;
    font-size: 22px;
    font-weight: 500;
    line-height: 1.3;
    color: var(--text);
  }
  .contact-icon {
    flex: none;
    width: 30px;
    height: 30px;
    fill: none;
    stroke: var(--violet);
    stroke-width: 1.8;
    stroke-linecap: round;
    stroke-linejoin: round;
  }
  .contact-address { width: 250px; }
</style>
</head>
<body>
  <section class="email-banner">
    <div class="ribbon-art" role="img" aria-label="Abstract translucent glass ribbon in blue, violet and pink"></div>

    <div class="brand">
      <span class="brand-dot"></span>
      <span class="brand-name">VEXOMARLIN</span>
    </div>

    <ul class="contact-list">
      <li class="contact-item">
        <svg class="contact-icon" viewBox="0 0 24 24" aria-hidden="true">
          <circle cx="12" cy="12" r="9"/>
          <path d="M3 12h18M12 3c2.5 2.5 3.8 5.5 3.8 9s-1.3 6.5-3.8 9M12 3c-2.5 2.5-3.8 5.5-3.8 9s1.3 6.5 3.8 9"/>
        </svg>
        <span>ml.vexomarlin.net</span>
      </li>
      <li class="contact-item">
        <svg class="contact-icon" viewBox="0 0 24 24" aria-hidden="true">
          <rect x="3" y="5" width="18" height="14" rx="1.5"/>
          <path d="M3.5 6l8.5 7 8.5-7"/>
        </svg>
        <span>hello@vexomarlin.net</span>
      </li>
      <li class="contact-item">
        <svg class="contact-icon" viewBox="0 0 24 24" aria-hidden="true">
          <path d="M5 3.5l3.2-.5 1.8 4.2-2.2 1.6a11 11 0 0 0 7.4 7.4l1.6-2.2 4.2 1.8-.5 3.2c-.2 1-1 1.5-2 1.5C10.5 20 4 13.5 3.5 5.5c0-1 .5-1.8 1.5-2z"/>
          <path d="M14 3.5a6.5 6.5 0 0 1 6.5 6.5M14 7a3 3 0 0 1 3 3"/>
        </svg>
        <span>+38-000-55-01-234</span>
      </li>
      <li class="contact-item">
        <svg class="contact-icon" viewBox="0 0 24 24" aria-hidden="true">
          <path d="M12 21s-6.5-6.2-6.5-11.2a6.5 6.5 0 0 1 13 0C18.5 14.8 12 21 12 21z"/>
          <circle cx="12" cy="9.8" r="2.4"/>
        </svg>
        <span class="contact-address">USA, 40712, 18 Harbor Lane</span>
      </li>
    </ul>
  </section>
</body>
</html>
```